New Web Site Design - Amber Ridge Telecom Solutions

We are looking for a completely new web site design. Amber Ridge Telecom Solutions is a full service company providing PBX and IP/Cloud Based phone systems. We also sell and install video camera surveillance systems and provide low voltage cabling services (CAT5 and CAT3). We are looking for something professional looking. We want to be able to showcase our vendor partners as well as be able to show photos of some of the work we have done. We will also want to be able to post PDF brochures as well as make changes to the website ourselves.

Target Market(s)

Commercial

Industry/Entity Type

Communication

Coding

Coded - Design and coding required

Number of Pages Required

5+ page

Font styles to use
Sans Serif

Colors
0455a3

Requirements
Must have
• Ability to upload PDF brochures
• Professional look and feel
• Ability to upload and easily insert job photos
• Thinking it should have at least 6 pages: Main page, phone systems and services page, carrier services page, video surveillance systems and service page, low voltage cabling services page, contact us page

```html
<!DOCTYPE html>
<html lang="en">
<head>
<meta charset="utf-8">
<title>Amber Ridge Telecom Solutions – Video Surveillance Systems</title>
<link rel="stylesheet" href="https://fonts.googleapis.com/css2?family=Arimo:wght@400;700&family=Roboto+Condensed:wght@400;700&family=Noto+Serif&display=swap">
<style>
:root{
  --brand:#0455a3;
  --brand-dark:#034a8e;
  --ink:#222;
  --text:#333;
  --white:#fff;
  --map:#48484a;
  --panel:rgba(150,150,155,.55);
  --field:rgba(200,200,205,.35);
  --bar:#8a8a8a;
}
*{box-sizing:border-box;margin:0;padding:0}
html,body{width:1200px;height:1121px;overflow:hidden;background:var(--white)}
body{position:relative;font-family:"Arimo",Arial,sans-serif;color:var(--text)}
.abs{position:absolute}

/* header */
.site-header{position:absolute;left:0;top:0;width:1200px;height:143px;background:var(--white)}
.header-band-left{left:0;top:0;width:127px;height:143px;background:var(--brand)}
.header-band-right{left:1116px;top:0;width:84px;height:143px;background:var(--brand)}
.brand-square{left:150px;top:62px;width:14px;height:14px;background:var(--brand-dark)}
.brand-name{left:174px;top:54px;font-size:30px;line-height:1;color:var(--brand-dark)}
.brand-sub{left:174px;top:86px;font-size:17px;line-height:1;color:var(--brand-dark);letter-spacing:.2px}
.follow{left:894px;top:23px;font-size:13px;color:var(--ink)}
.social{top:17px;width:28px;height:28px;border-radius:50%;background:#3a3a3a}
.brochure{left:682px;top:73px;width:242px;height:50px}
.brochure-icon{left:0;top:0;width:44px;height:50px}
.brochure-btn{left:41px;top:19px;width:201px;height:29px;background:var(--brand);color:var(--white);font-family:"Roboto Condensed",sans-serif;font-size:18px;line-height:29px;padding-left:16px}
.call-icon{left:938px;top:83px;width:32px;height:32px}
.call-label{left:976px;top:81px;font-size:15px;color:var(--ink)}
.call-number{left:976px;top:98px;font-size:22px;color:var(--brand)}

/* nav */
.main-nav{left:0;top:143px;width:1200px;height:52px;background:var(--brand);display:flex;font-family:"Noto Serif",serif;font-size:15px;color:var(--white)}
.main-nav a{display:block;color:var(--white);text-decoration:none;line-height:52px;border-right:1px solid rgba(255,255,255,.25)}
.main-nav a.current{color:#0b2c55;border-right:0}

/* hero */
.hero{left:0;top:195px;width:1200px;height:328px;background:linear-gradient(180deg,#8e9aa3 0%,#b9c2c4 40%,#c9b58a 68%,#6a6a66 100%)}

/* intro */
.intro-title{left:0;top:568px;width:1208px;text-align:center;font-family:"Roboto Condensed",sans-serif;font-size:30px;color:var(--ink);font-weight:400}
.intro-rule{left:296px;top:618px;width:615px;height:1px;background:#bbb}
.intro-rule-accent{left:567px;top:617px;width:73px;height:4px;background:var(--brand)}
.intro-text{left:120px;top:630px;width:968px;text-align:center;font-size:14px;line-height:24.5px;color:var(--text)}

/* footer */
.site-footer{left:0;top:722px;width:1200px;height:359px;background:var(--map)}
.contact-title{left:100px;top:740px;font-family:"Roboto Condensed",sans-serif;font-size:22px;color:var(--white);font-weight:400}
.contact-rule{left:100px;top:774px;width:336px;border-top:1px dashed #999}
.contact-item{left:133px;font-size:14px;line-height:20.5px;color:var(--white)}
.contact-icon{left:98px;width:18px;height:20px}
.footer-name{left:501px;top:948px;font-size:15px;color:rgba(255,255,255,.55);letter-spacing:.3px}

.inquiry{left:773px;top:741px;width:313px;height:327px;background:var(--panel);border-top:3px solid #ddd}
.inquiry-icon{left:16px;top:16px;width:40px;height:40px;border-radius:50%;background:var(--white)}
.inquiry-title{left:69px;top:19px;font-family:"Roboto Condensed",sans-serif;font-size:29px;color:var(--white);font-weight:400}
.inquiry-note{left:14px;top:79px;font-size:13.5px;color:var(--white)}
.field{left:13px;width:286px;height:34px;background:var(--field);color:var(--white);font-size:13px;padding:8px 12px}
.field-message{height:54px}
.submit{left:13px;top:270px;width:120px;height:33px;background:var(--brand);color:var(--white);font-weight:700;font-size:16px;letter-spacing:.5px;line-height:33px;padding-left:28px}

.copyright{left:0;top:1081px;width:1200px;height:40px;background:var(--bar);color:var(--white);font-size:13.5px;text-align:center;line-height:40px}
</style>
</head>
<body>

<header class="site-header">
  <div class="abs header-band-left"></div>
  <div class="abs header-band-right"></div>
  <div class="abs brand-square"></div>
  <div class="abs brand-name">Amber Ridge</div>
  <div class="abs brand-sub">TELECOM SOLUTIONS</div>

  <div class="abs follow">Follow Us On</div>
  <div class="abs social" style="left:986px"></div>
  <div class="abs social" style="left:1026px"></div>
  <div class="abs social" style="left:1067px"></div>

  <div class="abs brochure">
    <svg class="abs brochure-icon" viewBox="0 0 44 50" aria-hidden="true">
      <rect x="6" y="3" width="30" height="40" fill="#fff" stroke="#0455a3" stroke-width="2"/>
      <rect x="0" y="8" width="22" height="10" fill="#0455a3"/>
      <text x="3" y="16" font-family="Arimo,sans-serif" font-size="7" font-weight="700" fill="#fff">PDF</text>
      <path d="M21 21v13M15 28l6 6 6-6" fill="none" stroke="#0455a3" stroke-width="2"/>
      <rect x="3" y="43" width="40" height="6" fill="#0455a3"/>
    </svg>
    <div class="abs brochure-btn">Download Our Brochure</div>
  </div>

  <svg class="abs call-icon" viewBox="0 0 32 32" aria-hidden="true">
    <circle cx="16" cy="16" r="14" fill="none" stroke="#0455a3" stroke-width="2"/>
    <path d="M12 9c-2 2-2 6 1 10s7 5 9 4l1-2-3-2-2 1c-1-1-3-3-4-5l1-2-2-3z" fill="#0455a3"/>
  </svg>
  <div class="abs call-label">Call Us Today</div>
  <div class="abs call-number">555-201-4400</div>
</header>

<nav class="abs main-nav">
  <a style="padding:0 22px 0 100px">About Us</a>
  <a style="padding:0 24px 0 22px">Phone Systems &amp; Services</a>
  <a style="padding:0 22px">Low Voltage Cabling Service</a>
  <a style="padding:0 21px">Carrier Services</a>
  <a class="current" style="padding:0 21px">Video Surveillance Systems Service</a>
</nav>

<div class="abs hero" role="img" aria-label="Photo of a security control room with wall screens and monitors showing camera feeds"></div>

<main>
  <h1 class="abs intro-title">Video Surveillance Systems</h1>
  <div class="abs intro-rule"></div>
  <div class="abs intro-rule-accent"></div>
  <p class="abs intro-text">Amber Ridge installs and services surveillance packages. Our surveillance systems include; 1080p HD cameras, multiple terabit storage, real-time monitoring, and historical play-back and video archiving.</p>
</main>

<footer>
  <div class="abs site-footer" role="img" aria-label="Dark street map of the surrounding neighbourhood"></div>

  <h2 class="abs contact-title">Contact Details</h2>
  <div class="abs contact-rule"></div>

  <svg class="abs contact-icon" style="top:790px" viewBox="0 0 18 20" aria-hidden="true"><path d="M9 1a6 6 0 0 0-6 6c0 5 6 12 6 12s6-7 6-12a6 6 0 0 0-6-6z" fill="#fff"/><circle cx="9" cy="7" r="2.2" fill="#48484a"/></svg>
  <div class="abs contact-item" style="top:789px">Postal Address<br>Street Name, City Name State Zipcode</div>

  <svg class="abs contact-icon" style="top:846px" viewBox="0 0 18 20" aria-hidden="true"><path d="M5 2c-3 2-3 7 0 11s7 6 10 5l1-3-3-2-2 1c-2-1-4-4-5-6l1-2-2-4z" fill="#fff"/></svg>
  <div class="abs contact-item" style="top:844px;left:135px">Telephone<br>555-201-4400 &amp; Fax: 555-201-4411</div>

  <svg class="abs contact-icon" style="top:904px" viewBox="0 0 18 20" aria-hidden="true"><rect x="1" y="4" width="16" height="11" fill="#fff"/><path d="M1 4l8 6 8-6" fill="none" stroke="#48484a" stroke-width="1.5"/></svg>
  <div class="abs contact-item" style="top:900px">Email<br>Information and Support: inquiry@amberridge.com</div>

  <svg class="abs contact-icon" style="top:958px" viewBox="0 0 18 20" aria-hidden="true"><circle cx="9" cy="10" r="8" fill="#fff"/></svg>
  <div class="abs contact-item" style="top:956px">Social Page<br>www.socialpage.example/amberridge</div>

  <svg class="abs contact-icon" style="top:1014px" viewBox="0 0 18 20" aria-hidden="true"><circle cx="9" cy="10" r="8" fill="#fff"/></svg>
  <div class="abs contact-item" style="top:1012px">Photo Feed<br>www.photofeed.example/amberridge</div>

  <div class="abs footer-name">Amber Ridge Telecom Solutions</div>

  <form class="abs inquiry">
    <div class="abs inquiry-icon">
      <svg viewBox="0 0 40 40" width="40" height="40" aria-hidden="true"><path d="M14 11c-3 2-3 8 1 13s9 7 12 5l1-3-4-3-2 1c-2-1-4-4-5-6l1-2-4-5z" fill="#0455a3"/></svg>
    </div>
    <h2 class="abs inquiry-title">Quick Inquiry</h2>
    <p class="abs inquiry-note">Lorem ipsum dolor sit amet, consectetuer</p>
    <div class="abs field" style="top:103px">Name</div>
    <div class="abs field" style="top:140px">Email</div>
    <div class="abs field" style="top:178px">Phone</div>
    <div class="abs field field-message" style="top:215px">Message</div>
    <div class="abs submit">SUBMIT</div>
  </form>

  <div class="abs copyright">Copyright© 2016&nbsp; Amber Ridge Telecom Solutions&nbsp; All Rights Reserved</div>
</footer>

</body>
</html>
```